Marketing graphics & images for Shopify store

I need someone to create some graphics/images for a coffee sales shopify storefront incorporating my existing logo and want variations on the logo colour so it blends with background images. Freelancer is to provide suitable coffee product related images and designs. Want a catalogue of images i can rotate and use on the storefront.

The tagline on the storefront page " a fresh start to your day" will change - i will update brief accordingly.

Font styles to use
Script

Requirements
Must have
• A variety of images sizes and graphics to be rotated for website marketing purposes.

Also would like some additional logo files with varying colors - ie black version, white version. Darker more chocolate brown version. Need to be logo quality

```html
<!DOCTYPE html>
<html lang="en">
<head>
<meta charset="utf-8">
<title>Special Delicious Coffee – Banner</title>
<link rel="stylesheet" href="https://fonts.googleapis.com/css2?family=Anton&family=Kaushan+Script&family=Kalam:wght@700&family=Montserrat:wght@700;800&display=swap">
<style>
  :root {
    --backdrop: #7f4433;
    --banner-dark: #2b170f;
    --banner-mid: #6a3828;
    --banner-light: #80432f;
    --photo-dark: #1e1714;
    --photo-mid: #3a2620;
    --accent: #ffad0a;
    --white: #ffffff;
    --ink: #1d120c;
    --brand-tan: #a8703e;
    --bean-light: #c87a4a;
    --bean-dark: #8a3f1e;
  }
  html, body {
    margin: 0;
    width: 1200px;
    height: 457px;
    overflow: hidden;
    background: var(--backdrop);
  }
  .banner {
    position: absolute;
    left: 114px;
    top: 49px;
    width: 973px;
    height: 359px;
    overflow: hidden;
    background:
      radial-gradient(ellipse 55% 75% at 52% 55%, var(--banner-light) 0%, var(--banner-mid) 45%, transparent 100%),
      linear-gradient(90deg, var(--banner-dark) 0%, var(--banner-mid) 45%, var(--banner-mid) 70%, var(--banner-dark) 100%);
    box-shadow: 0 8px 14px rgba(40, 18, 10, 0.55);
  }
  .bean-photo {
    position: absolute;
    border-radius: 50%;
    background: radial-gradient(circle at 45% 40%, var(--bean-light) 0%, var(--bean-dark) 55%, rgba(90, 40, 20, 0) 100%);
    filter: blur(2px);
  }
  .bean-photo--left { left: -30px; top: 83px; width: 71px; height: 92px; }
  .bean-photo--bottom { left: 282px; top: 317px; width: 78px; height: 60px; filter: none; }
  .bean-photo--top-right { left: 863px; top: -24px; width: 116px; height: 90px; }

  .coffee-photo {
    position: absolute;
    left: 462px;
    top: 12px;
    width: 332px;
    height: 332px;
    background: radial-gradient(ellipse 50% 50% at 50% 50%, var(--photo-dark) 0%, var(--photo-mid) 55%, rgba(58, 38, 32, 0) 100%);
  }

  .headline {
    position: absolute;
    margin: 0;
    white-space: nowrap;
    line-height: 1;
    transform: translate(-50%, -50%) rotate(var(--tilt));
  }
  .headline--script {
    left: 193px;
    top: 108px;
    --tilt: -24deg;
    font-family: "Kaushan Script", cursive;
    font-weight: 400;
    font-size: 70px;
    color: var(--white);
  }
  .headline--main {
    left: 247px;
    top: 156px;
    --tilt: -15deg;
    font-family: "Anton", sans-serif;
    font-weight: 400;
    font-size: 52px;
    letter-spacing: 1px;
    color: var(--accent);
  }
  .headline--offer {
    left: 314px;
    top: 180px;
    --tilt: -16deg;
    font-family: "Kalam", cursive;
    font-weight: 700;
    font-size: 26px;
    letter-spacing: 1.5px;
    color: var(--white);
  }
  .swoosh {
    position: absolute;
    left: 0;
    top: 0;
    width: 973px;
    height: 359px;
    pointer-events: none;
  }
  .shop-button {
    position: absolute;
    left: 187px;
    top: 257px;
    width: 113px;
    height: 26px;
    border-radius: 4px;
    background: var(--accent);
    color: var(--ink);
    font-family: "Montserrat", sans-serif;
    font-weight: 800;
    font-size: 10.5px;
    line-height: 26px;
    text-align: center;
    text-decoration: none;
    letter-spacing: 0.2px;
  }
  .discount {
    position: absolute;
    left: 802px;
    top: 124px;
    width: 110px;
    height: 100px;
  }
  .discount__value {
    position: absolute;
    left: 861px;
    top: 168px;
    transform: translate(-50%, -50%) rotate(24deg);
    font-family: "Montserrat", sans-serif;
    font-weight: 800;
    font-size: 30px;
    color: var(--accent);
    white-space: nowrap;
  }
  .discount__label {
    position: absolute;
    left: 852px;
    top: 193px;
    transform: translate(-50%, -50%) rotate(24deg);
    font-family: "Montserrat", sans-serif;
    font-weight: 800;
    font-size: 15px;
    color: var(--white);
    white-space: nowrap;
  }
  .brand {
    position: absolute;
    left: 834px;
    top: 306px;
    display: flex;
    align-items: center;
    gap: 6px;
  }
  .brand__dot {
    width: 22px;
    height: 22px;
    border-radius: 50%;
    background: var(--brand-tan);
  }
  .brand__name {
    font-family: "Kaushan Script", cursive;
    font-size: 21px;
    color: var(--brand-tan);
    white-space: nowrap;
  }
</style>
</head>
<body>
  <main class="banner">
    <div class="bean-photo bean-photo--left" role="img" aria-label="Blurred roasted coffee bean close-up"></div>
    <div class="bean-photo bean-photo--top-right" role="img" aria-label="Blurred roasted coffee bean close-up"></div>
    <div class="bean-photo bean-photo--bottom" role="img" aria-label="Roasted coffee bean close-up"></div>

    <div class="coffee-photo" role="img" aria-label="Top view of a cup of black coffee on a dark notebook with scattered coffee beans"></div>

    <p class="headline headline--script">Special</p>
    <h1 class="headline headline--main">DELICIOUS COFFEE</h1>
    <p class="headline headline--offer">Today's Super Offer</p>

    <svg class="swoosh" viewBox="0 0 973 359" aria-hidden="true">
      <path d="M72 243 Q120 228 164 214" stroke="var(--accent)" stroke-width="3" stroke-linecap="round" fill="none"/>
      <path d="M170 212 L182 209" stroke="var(--accent)" stroke-width="4" stroke-linecap="round" fill="none"/>
    </svg>

    <a class="shop-button" href="#">SHOP NOW</a>

    <svg class="discount" viewBox="0 0 120 110" aria-hidden="true">
      <path d="M10 85 C-2 60 4 25 35 10 C65 -4 108 6 116 40 C122 70 95 97 62 99 C45 100 33 96 22 90 L3 92 L14 80 Z"
            fill="none" stroke="var(--white)" stroke-width="3.5" stroke-linejoin="round"/>
    </svg>
    <span class="discount__value">10%</span>
    <span class="discount__label">OFF</span>

    <div class="brand">
      <span class="brand__dot"></span>
      <span class="brand__name">Brisa Roast</span>
    </div>
  </main>
</body>
</html>
```